Experienced and Professional Marriage Celebrant

I need a web design for my services as a marriage celebrant in the Sydney area. I want people to have the impression I am a modern and professional marriage celebrant who can tailor a wedding ceremony and execute the ceremony with a high level of care and accommodate and adapt to any style of wedding and personalities of couples. I like a mint and pink and black theme and I am not sure whether to use the professional photos of me, might be too stiff! But would like to see ideas you can come up with. Happy to use other photos you might have

Reason: I have haven't been able to respond as quickly as I would have liked this last week to comments so extending a few days. Thanks

```html
<!DOCTYPE html>
<html lang="en">
<head>
<meta charset="utf-8">
<title>Nora Whitfield Celebrant</title>
<link href="https://fonts.googleapis.com/css2?family=Arimo:wght@400;700&display=swap" rel="stylesheet">
<style>
  :root {
    --pink: #ee168c;
    --pink-soft: #f5a3cf;
    --pink-active: #f45aa8;
    --ink: #111111;
    --grey-text: #8a8a8a;
    --link: #2b2a80;
    --footer-bg: #1c1c1c;
    --white: #ffffff;
  }
  * { box-sizing: border-box; margin: 0; padding: 0; }
  html, body { width: 756px; height: 1200px; overflow: hidden; }
  body {
    position: relative;
    font-family: "Arimo", Arial, sans-serif;
    color: var(--ink);
    background:
      radial-gradient(ellipse 120px 420px at 0 520px, rgba(238,22,140,.55), transparent 70%),
      radial-gradient(ellipse 90px 110px at 700px 40px, rgba(245,130,190,.55), transparent 75%),
      radial-gradient(ellipse 130px 500px at 756px 760px, rgba(238,22,140,.6), transparent 70%),
      linear-gradient(to bottom, var(--white) 0, var(--white) 700px, #f7b5d8 950px, var(--pink) 1066px);
  }
  .brand {
    position: absolute; left: 0; top: 28px; width: 756px;
    text-align: center; font-size: 26px; font-weight: 400; color: var(--ink);
    letter-spacing: .5px;
  }
  .main-nav {
    position: absolute; left: 49px; top: 97px; width: 662px; height: 34px;
    background: var(--pink); display: flex; padding-left: 70px;
  }
  .main-nav a {
    color: var(--white); text-decoration: none; font-size: 18px;
    line-height: 34px; padding: 0 8px;
  }
  .main-nav a.is-active { background: var(--pink-active); padding: 0 12px; }
  .hero {
    position: absolute; left: 49px; top: 133px; width: 662px; height: 225px;
    background: linear-gradient(to bottom, #6b5236 0%, #4a3a26 55%, #8a6d4a 80%, #6c7a86 100%);
    box-shadow: 0 2px 4px rgba(0,0,0,.3);
  }
  .content-panel {
    position: absolute; left: 47px; top: 371px; width: 665px; height: 695px;
    background: linear-gradient(to bottom, var(--white), #e4e4e4);
    box-shadow: 0 0 3px rgba(0,0,0,.25);
  }
  .section-title { position: absolute; font-size: 22px; font-weight: 400; }
  .rule { position: absolute; height: 2px; background: var(--pink); }
  .body-copy { position: absolute; font-size: 18px; line-height: 22px; }
  .photo { position: absolute; }
  .read-more { color: var(--link); text-decoration: none; }
  .testimonial-photo {
    position: absolute; width: 86px; height: 86px; border-radius: 50%;
    background: linear-gradient(135deg, #5b4a38, #a07a58);
    box-shadow: 0 1px 3px rgba(0,0,0,.4);
  }
  .testimonial-name { position: absolute; font-size: 11px; color: var(--pink); }
  .testimonial-quote { position: absolute; font-size: 11px; line-height: 13px; color: var(--grey-text); }
  .site-footer {
    position: absolute; left: 0; top: 1066px; width: 756px; height: 134px;
    background: var(--footer-bg); border-top: 6px solid var(--pink);
    color: var(--white); font-size: 14px; line-height: 17px;
  }
  .footer-col { position: absolute; top: 22px; }
  .social-links { display: flex; gap: 3px; margin: 3px 0 0 11px; }
  .social-links span { width: 9px; height: 9px; background: #bdbdbd; }
</style>
</head>
<body>
  <header>
    <div class="brand">Nora Whitfield Celebrant</div>
    <nav class="main-nav">
      <a class="is-active" href="#">Home</a>
      <a href="#">About</a>
      <a href="#">Ceremony</a>
      <a href="#">Gallery</a>
      <a href="#">Testimonials</a>
      <a href="#">Contact</a>
    </nav>
  </header>

  <div class="hero" role="img" aria-label="Smiling couple embracing by the water at sunset"></div>

  <main class="content-panel">
    <h2 class="section-title" style="left:20px; top:13px;">Welcome</h2>
    <div class="rule" style="left:11px; top:45px; width:507px;"></div>
    <p class="body-copy" style="left:8px; top:58px; width:500px;">Welcome to my services as a marriage celebrant in the Sydney area. I want people to have the impression I am a modern and professional marriage celebrant who can tailor a wedding ceremony and execute the ceremony with a high level of care and accommodate and adapt to any style of wedding and personalities of couples. I like a mint and pink and black theme I But would like to see ideas you can come up with Happy to use other photos you might have.</p>
    <div class="photo" style="left:529px; top:40px; width:126px; height:190px; background:linear-gradient(to bottom,#7fa9d6,#c9b8b0 60%,#6a6a72);" role="img" aria-label="Celebrant leading a seaside wedding ceremony"></div>

    <h2 class="section-title" style="left:334px; top:278px;">Services</h2>
    <div class="rule" style="left:125px; top:307px; width:506px;"></div>
    <div class="photo" style="left:17px; top:309px; width:83px; height:125px; background:linear-gradient(160deg,#6b5544,#cbb9a4 55%,#8a7a68);" role="img" aria-label="Couple holding hands with a bridal bouquet"></div>
    <p class="body-copy" style="left:125px; top:319px; width:535px;">My services as a marriage celebrant in the Sydney area. I want people to have the impression I am a modern and professional marriage celebrant who can tailor a wedding ceremony and execute the ceremony with a high level of care and accommodate and adapt to any style of wedding and personalities of couples. <a class="read-more" href="#">Read More</a></p>

    <h2 class="section-title" style="left:275px; top:483px;">Tetimonials</h2>
    <div class="rule" style="left:36px; top:518px; width:607px;"></div>

    <div class="testimonial-photo" style="left:12px; top:534px;" role="img" aria-label="Portrait of a happy couple"></div>
    <div class="testimonial-name" style="left:14px; top:623px;">Mr. / Mrs. A &amp; B</div>
    <p class="testimonial-quote" style="left:119px; top:563px;">Ms. Nora Whitfield is very professional<br>we are very happy</p>

    <div class="testimonial-photo" style="left:377px; top:534px;" role="img" aria-label="Portrait of a happy couple"></div>
    <div class="testimonial-name" style="left:379px; top:623px;">Mr. / Mrs. A &amp; B</div>
    <p class="testimonial-quote" style="left:480px; top:563px;">Ms. Nora Whitfield is very professional<br>we are very happy</p>
  </main>

  <footer class="site-footer">
    <div class="footer-col" style="left:72px;">Home<br>About<br>Ceremony<br>Gallery</div>
    <div class="footer-col" style="left:225px;">Contact<br>555-014-2290<br>Address: Sydney<br>Email: nora@example.com</div>
    <div class="footer-col" style="left:461px;">Follow Us
      <div class="social-links" aria-label="Social links"><span></span><span></span><span></span></div>
    </div>
  </footer>
</body>
</html>
```